Create American style design suitable for consumers in Europe and America

We need a professional universal neutral design, which can be applied to all personal care tools, regardless of male and female, and the color matching needs to be matched by designers themselves.
Updates

设计质量低

Target Market(s)

Europe and America

Industry/Entity Type

personal care tools

Font styles to use
Serif
Sans Serif
Script

Requirements
Must have
• personal beauty care tool,like nail clipper,tweezer,scissors
Nice to have
• The copywriter plans on the packaging design can be applied to all personal care tools
Should not have
• Not designed for a single product, but for a whole personal care tool

```html
<!DOCTYPE html>
<html lang="en">
<head>
<meta charset="utf-8">
<title>Kelva Care – Personal Care Tool Card</title>
<link rel="stylesheet" href="https://fonts.googleapis.com/css2?family=Montserrat:wght@300;400;500&display=swap">
<style>
  :root {
    --page: #ffffff;
    --card: #e6e9ea;
    --card-edge: #b9c2c7;
    --window: #f6f6f6;
    --window-edge: #b9c2c7;
    --ring: #ffffff;
    --accent: #2f6f7e;
    --ink: #1d262c;
    --motif-a: #dde2e4;
    --motif-b: #c3ccd1;
    --product-a: #e9e9ea;
    --product-b: #9b9a9b;
  }
  html, body {
    margin: 0;
    width: 1200px;
    height: 1200px;
    overflow: hidden;
    background: var(--page);
  }
  .canvas {
    position: relative;
    width: 1200px;
    height: 1200px;
  }
  .artwork {
    position: absolute;
    inset: 0;
  }
  .brand {
    position: absolute;
    left: 0;
    right: 0;
    top: 196px;
    text-align: center;
    font-family: "Montserrat", sans-serif;
    color: var(--ink);
  }
  .brand-name {
    display: block;
    font-weight: 400;
    font-size: 66px;
    line-height: 1;
    letter-spacing: 1px;
  }
  .brand-tagline {
    display: block;
    margin-top: 8px;
    font-weight: 400;
    font-size: 19px;
    line-height: 1;
    letter-spacing: 1px;
  }
</style>
</head>
<body>
<div class="canvas">
  <svg class="artwork" width="1200" height="1200" viewBox="0 0 1200 1200">
    <defs>
      <linearGradient id="motifTone" x1="0" y1="0" x2="0" y2="1">
        <stop offset="0" stop-color="var(--motif-a)"/>
        <stop offset="1" stop-color="var(--motif-b)"/>
      </linearGradient>
      <linearGradient id="productTone" x1="0" y1="0" x2="1" y2="1">
        <stop offset="0" stop-color="var(--product-a)"/>
        <stop offset="0.5" stop-color="var(--product-b)" stop-opacity="0.35"/>
        <stop offset="1" stop-color="var(--product-a)"/>
      </linearGradient>
      <path id="sloganArc" d="M 363 330 A 240 240 0 0 1 843 330"/>
    </defs>

    <!-- card -->
    <rect class="card" x="284" y="64" width="639" height="1078" fill="var(--card)" stroke="var(--card-edge)" stroke-width="4"/>

    <!-- lower decorative motif area -->
    <rect class="motif" x="286" y="820" width="635" height="320" fill="url(#motifTone)" role="img" aria-label="Soft flowing line pattern along the bottom of the card"/>

    <!-- outer ring capsule -->
    <rect class="ring" x="381" y="137" width="445" height="935" rx="222.5" fill="var(--card)" stroke="var(--ring)" stroke-width="3"/>

    <!-- product window -->
    <rect class="window" x="402" y="161" width="404" height="884" rx="202" fill="var(--window)" stroke="var(--window-edge)" stroke-width="4"/>

    <!-- product photo area -->
    <rect class="product" x="430" y="370" width="330" height="520" rx="24" fill="url(#productTone)" opacity="0.7" role="img" aria-label="Photo of the stainless steel personal care tool inside the pack"/>

    <!-- accent bars -->
    <rect class="accent-bar" x="376" y="340" width="13" height="158" rx="6.5" fill="var(--accent)"/>
    <rect class="accent-bar" x="816" y="671" width="13" height="158" rx="6.5" fill="var(--accent)"/>

    <!-- accent dots -->
    <circle class="accent-dot" cx="306" cy="1067" r="9" fill="var(--accent)"/>
    <circle class="accent-dot" cx="900" cy="1066" r="9" fill="var(--accent)"/>

    <!-- slogan on arc -->
    <text class="slogan" font-family="Montserrat, sans-serif" font-weight="400" font-size="29" letter-spacing="1" fill="var(--ring)">
      <textPath href="#sloganArc" startOffset="50%" text-anchor="middle">- PERSONAL CARE TOOLS - PRECISION EVERY DAY -</textPath>
    </text>
  </svg>

  <div class="brand">
    <span class="brand-name">Kelva</span>
    <span class="brand-tagline">Kelva Care</span>
  </div>
</div>
</body>
</html>
```